Bellmont Planners, LLC Stationary

Bellmont Planners, LLC is a new financial planning and consulting company. We are looking for designs on business cards, letterhead, envelopes, and anything else that would be useful. Our preference for business card design is two sided. We are looking for a professional and clean look with incorporating the logo and patriotic feel. Thank you to all who participate and good luck!

```html
<!DOCTYPE html>
<html lang="en">
<head>
<meta charset="utf-8">
<title>Bellmont Planners, LLC — Business Card</title>
<link rel="stylesheet" href="https://fonts.googleapis.com/css2?family=Montserrat:wght@600&family=Open+Sans:wght@400;600&display=swap">
<style>
  :root {
    --backdrop: #e9e7e4;
    --card: #131416;
    --blue: #2f5c9e;
    --red: #c7333b;
    --ink: #e6e6e6;
    --muted: #8a8f98;
    --rule: #5a5e66;
  }
  * { box-sizing: border-box; margin: 0; padding: 0; }
  html, body {
    width: 1200px; height: 814px; overflow: hidden;
    background: var(--backdrop);
  }
  .stage {
    position: relative; width: 1200px; height: 814px;
    display: flex; align-items: center; justify-content: center; gap: 40px;
  }
  .card {
    position: relative; width: 520px; height: 297px;
    background: var(--card);
    box-shadow: 0 6px 18px rgba(0,0,0,0.18);
  }
  .brand {
    display: flex; align-items: center; gap: 10px;
  }
  .brand-mark {
    width: 16px; height: 16px; border-radius: 50%;
    background: var(--red); flex: none;
  }
  .brand-name {
    font-family: "Montserrat", sans-serif; font-weight: 600;
    color: var(--blue); letter-spacing: 0.02em; line-height: 1;
  }
  .brand-tagline {
    font-family: "Open Sans", sans-serif; font-size: 7px;
    color: var(--muted); text-transform: uppercase; letter-spacing: 0.16em;
    margin-top: 6px;
  }

  /* Front: logo + contact */
  .card-front .brand-block {
    position: absolute; left: 34px; top: 128px; width: 210px;
  }
  .card-front .brand-name { font-size: 16px; }
  .card-front .brand-tagline { padding-left: 26px; }
  .card-front .divider {
    position: absolute; left: 262px; top: 74px; width: 1px; height: 150px;
    background: var(--rule);
  }
  .contact {
    position: absolute; left: 282px; top: 74px;
    font-family: "Open Sans", sans-serif; color: var(--ink);
  }
  .contact-name { font-size: 15px; font-weight: 600; color: var(--blue); line-height: 1.1; }
  .contact-title { font-size: 11px; color: var(--red); margin-bottom: 6px; }
  .contact-address { font-size: 11px; line-height: 1.45; margin-bottom: 2px; }
  .contact-list { list-style: none; font-size: 11px; line-height: 1.5; }
  .contact-list li { display: flex; align-items: center; gap: 7px; }
  .contact-list svg { width: 10px; height: 10px; fill: var(--blue); flex: none; }

  /* Back: centered logo + web */
  .card-back .brand-block {
    position: absolute; left: 0; right: 0; top: 108px;
    display: flex; flex-direction: column; align-items: center;
  }
  .card-back .brand-name { font-size: 24px; }
  .card-back .brand-tagline { font-size: 8px; margin-top: 8px; }
  .card-back .web {
    position: absolute; left: 0; right: 0; top: 208px; text-align: center;
    font-family: "Open Sans", sans-serif; font-size: 10px; color: var(--ink);
    letter-spacing: 0.32em;
  }
</style>
</head>
<body>
<main class="stage">

  <section class="card card-front" aria-label="Business card front">
    <div class="brand-block">
      <div class="brand">
        <span class="brand-mark"></span>
        <span class="brand-name">Bellmont Planners, LLC</span>
      </div>
      <div class="brand-tagline">Financial Planning and Consulting</div>
    </div>
    <div class="divider"></div>
    <div class="contact">
      <div class="contact-name">Daniel Reyes</div>
      <div class="contact-title">CEO/Founder</div>
      <div class="contact-address">4120 Willow Crest Drive<br>Juneau, Alaska 99801</div>
      <ul class="contact-list">
        <li>
          <svg viewBox="0 0 10 10"><path d="M2 0.5l2 2-1 1.2c.6 1.3 1.6 2.3 2.9 2.9L7 5.6l2 2-1.2 1.6C4.3 9 1 5.7.8 2.2z"/></svg>
          555 210 4187
        </li>
        <li>
          <svg viewBox="0 0 10 10"><rect x="2.5" y="0.5" width="5" height="3"/><rect x="0.5" y="3.5" width="9" height="4.5" rx="0.8"/><rect x="2.5" y="7" width="5" height="2.5"/></svg>
          555 362 7051
        </li>
        <li>
          <svg viewBox="0 0 10 10"><path d="M0.5 2h9v6h-9z M0.5 2l4.5 3.5L9.5 2" stroke="#131416" stroke-width="0.8"/></svg>
          hello@bellmontplanners.com
        </li>
        <li>
          <svg viewBox="0 0 10 10"><circle cx="5" cy="5" r="4.5"/><path d="M0.5 5h9M5 0.5c-2.2 2.5-2.2 6.5 0 9M5 0.5c2.2 2.5 2.2 6.5 0 9" stroke="#131416" stroke-width="0.7" fill="none"/></svg>
          www.bellmontplanners.com
        </li>
      </ul>
    </div>
  </section>

  <section class="card card-back" aria-label="Business card back">
    <div class="brand-block">
      <div class="brand">
        <span class="brand-mark"></span>
        <span class="brand-name">Bellmont Planners, LLC</span>
      </div>
      <div class="brand-tagline">Financial Planning and Consulting</div>
    </div>
    <div class="web">www.bellmontplanners.com</div>
  </section>

</main>
</body>
</html>
```